Acupuncture Medspa needs a business card design

I need a business card design that looks professional, has a spa-like quality and can offer a promo on the back. Initial promo is "First session free". The tagline of NeedleNook is: Refresh, Restore, Rejuvenate.

NeedleNook is a membership-based acupuncture medspa that offers acupuncture, cupping, and herbal therapies. Members choose between the "Refresh" membership which is for stress relief, or "Restore" which is for treating health conditions, and lastly "Rejuvenate" which is for natural facial enhancement.

Industry/Entity Type

Health And Wellness

Contact Information for Business Card

Coral Haskins, MAC, L.Ac.
612-555-0193
www.needlenook-example.com

Font styles to use
Serif
Sans Serif

Colors

Designer to choose colors to be used in the design.

Requirements
Must have
• The project must have NeedleNook logo, promo on the back, and contact information
Nice to have
• I would like to see the colors of the logo used.

```html
<!DOCTYPE html>
<html lang="en">
<head>
<meta charset="UTF-8">
<title>NeedleNook Business Card</title>
<link href="https://fonts.googleapis.com/css2?family=Montserrat:wght@400;500&family=Oswald:wght@600&family=Work+Sans:wght@400;500&display=swap" rel="stylesheet">
<style>
  :root {
    --backdrop-top: #1c1c1c;
    --backdrop-bottom: #070707;
    --card: #222222;
    --card-edge: #2a2a2a;
    --ink-deep: #0d0d0d;
    --ink-silver: #e6e6e6;
    --ink-muted: #7a7a7a;
    --rule: #555555;
  }
  * { margin: 0; padding: 0; box-sizing: border-box; }
  html, body { width: 1200px; height: 900px; overflow: hidden; }
  body {
    background: radial-gradient(ellipse at 50% 30%, var(--backdrop-top), var(--backdrop-bottom) 75%);
    display: flex;
    flex-direction: column;
    align-items: center;
    justify-content: center;
    gap: 40px;
  }
  .card {
    width: 660px;
    height: 377px;
    background: linear-gradient(135deg, var(--card) 0%, var(--card-edge) 70%, #303030 100%);
    box-shadow: 0 14px 30px rgba(0,0,0,0.6);
    position: relative;
  }
  .card-front {
    display: flex;
    flex-direction: column;
    align-items: center;
    justify-content: center;
    gap: 22px;
  }
  .logo {
    display: flex;
    align-items: center;
    gap: 14px;
  }
  .logo-mark {
    width: 46px; height: 46px;
    border: 2px solid var(--ink-silver);
    border-radius: 50%;
  }
  .logo-name {
    font-family: "Montserrat", sans-serif;
    font-weight: 400;
    font-size: 46px;
    letter-spacing: 3px;
    color: var(--ink-silver);
  }
  .tagline {
    font-family: "Work Sans", sans-serif;
    font-size: 14px;
    letter-spacing: 4px;
    text-transform: uppercase;
    color: var(--ink-muted);
  }
  .promo {
    position: absolute;
    left: 44px;
    top: 40px;
    font-family: "Montserrat", sans-serif;
    font-weight: 500;
    font-size: 15px;
    letter-spacing: 3px;
    text-transform: uppercase;
    color: var(--ink-silver);
  }
  .card-back .identity {
    position: absolute;
    right: 370px;
    top: 128px;
    text-align: right;
  }
  .person-name {
    font-family: "Oswald", sans-serif;
    font-weight: 600;
    font-size: 38px;
    line-height: 1;
    color: var(--ink-deep);
    text-transform: uppercase;
    text-shadow: 0 1px 0 rgba(255,255,255,0.22), 0 -1px 0 rgba(0,0,0,0.6);
  }
  .person-role {
    font-family: "Work Sans", sans-serif;
    font-size: 17px;
    color: var(--ink-muted);
    margin-top: 4px;
  }
  .divider {
    position: absolute;
    left: 307px;
    top: 140px;
    width: 1px;
    height: 70px;
    background: var(--rule);
  }
  .contact-list {
    position: absolute;
    left: 330px;
    top: 135px;
    list-style: none;
    font-family: "Work Sans", sans-serif;
    font-size: 18px;
    color: var(--ink-silver);
    line-height: 26px;
  }
  .contact-list li { display: flex; align-items: center; gap: 8px; }
  .contact-list svg { width: 12px; height: 12px; flex: none; }
  .address {
    position: absolute;
    left: 44px;
    bottom: 44px;
    font-family: "Work Sans", sans-serif;
    font-size: 19px;
    color: var(--ink-deep);
    text-shadow: 0 1px 0 rgba(255,255,255,0.2);
  }
</style>
</head>
<body>
  <section class="card card-front">
    <div class="logo">
      <span class="logo-mark"></span>
      <span class="logo-name">NEEDLENOOK</span>
    </div>
    <p class="tagline">Refresh, Restore, Rejuvenate</p>
  </section>

  <section class="card card-back">
    <p class="promo">First session free</p>
    <div class="identity">
      <p class="person-name">Coral Haskins</p>
      <p class="person-role">Director</p>
    </div>
    <span class="divider"></span>
    <ul class="contact-list">
      <li>
        <svg viewBox="0 0 12 12" fill="none" stroke="#e6e6e6" stroke-width="1.3"><path d="M2.5 1.5h2l1 2.5-1.3 1a6 6 0 0 0 2.8 2.8l1-1.3 2.5 1v2a1 1 0 0 1-1 1A8.5 8.5 0 0 1 1.5 2.5a1 1 0 0 1 1-1z"/></svg>
        612-555-0193
      </li>
      <li>
        <svg viewBox="0 0 12 12" fill="none" stroke="#e6e6e6" stroke-width="1.2"><rect x="1" y="2.5" width="10" height="7"/><path d="M1 2.5l5 4 5-4"/></svg>
        info@needlenook-example.com
      </li>
      <li>
        <svg viewBox="0 0 12 12" fill="none" stroke="#e6e6e6" stroke-width="1.1"><circle cx="6" cy="6" r="5"/><ellipse cx="6" cy="6" rx="2.2" ry="5"/><path d="M1 6h10"/></svg>
        www.needlenook-example.com
      </li>
    </ul>
    <p class="address">1870 Willow Bend Road Lakemont, FL 33999</p>
  </section>
</body>
</html>
```